Business Card Design Harbor of Calm

mental health provider
contemporary
warmth
inviting

Target Market(s)

mental health clients adults

Industry/Entity Type

Mental Health

Contact Information for Business Card

Danielle Korrish PMHNP
2938 SW Fennick Ave
Suite 340C
Portland OR 97225
Fax 503-418-9152
Tel 503-418-9267
Email danielle@dkorrish.com
Website dkorrish.com

Requirements
Nice to have
• see above
Should not have
• no medical logos

```html
<!DOCTYPE html>
<html lang="en">
<head>
<meta charset="utf-8">
<title>Harbor of Calm – Business Card</title>
<link rel="stylesheet" href="https://fonts.googleapis.com/css2?family=Eagle+Lake&family=Cabin:wght@400;600&display=swap">
<style>
  :root {
    --bg: #ece8e1;
    --brown: #2a2115;
    --leaf: #cfe5a7;
    --leaf-band: #a7cf6d;
    --text-green: #a9d27a;
    --shadow: rgba(40, 30, 15, 0.25);
  }
  * { box-sizing: border-box; margin: 0; padding: 0; }
  html, body {
    width: 1200px; height: 1000px; overflow: hidden;
    background: var(--bg);
  }
  .canvas { position: relative; width: 1200px; height: 1000px; }
  .card {
    position: absolute; left: 250px;
    width: 700px; height: 400px; overflow: hidden;
    box-shadow: 0 10px 28px var(--shadow);
  }
  .card--front { top: 70px; }
  .card--back { top: 530px; }
  .card__art { position: absolute; inset: 0; width: 100%; height: 100%; }

  .front__name {
    position: absolute; left: 55px; top: 250px;
    font-family: "Eagle Lake", serif;
    color: var(--text-green);
    line-height: 1.2;
    white-space: nowrap;
  }
  .front__person { font-size: 42px; }
  .front__title { font-size: 28px; padding-left: 110px; }

  .back__name {
    position: absolute; right: 60px; top: 130px;
    text-align: right;
    font-family: "Eagle Lake", serif;
    color: var(--text-green);
    white-space: nowrap;
  }
  .back__person { font-size: 34px; }
  .back__title { font-size: 22px; padding-right: 40px; }

  .back__contact {
    position: absolute; left: 55px; top: 215px;
    list-style: none;
    font-family: "Cabin", sans-serif;
    font-size: 18px; line-height: 1.4;
    color: var(--text-green);
    white-space: nowrap;
  }
  .back__contact .label { font-weight: 600; }
</style>
</head>
<body>
<main class="canvas">

  <section class="card card--front" aria-label="Business card front">
    <svg class="card__art" viewBox="0 0 700 400" preserveAspectRatio="none">
      <rect width="700" height="400" fill="var(--leaf)" role="img" aria-label="Soft green leaf pattern background"/>
      <path d="M0,92 C230,70 440,150 700,320 L700,400 L0,400 Z" fill="var(--leaf-band)"/>
      <path d="M0,118 C230,96 430,180 700,350 L700,400 L0,400 Z" fill="var(--brown)"/>
    </svg>
    <div class="front__name">
      <div class="front__person">Danielle Korrish</div>
      <div class="front__title">PMHNP, Inc.</div>
    </div>
  </section>

  <section class="card card--back" aria-label="Business card back">
    <svg class="card__art" viewBox="0 0 700 400" preserveAspectRatio="none">
      <rect width="700" height="400" fill="var(--leaf)" role="img" aria-label="Soft green leaf pattern background"/>
      <path d="M0,92 C200,70 430,40 700,62 L700,400 L0,400 Z" fill="var(--leaf-band)"/>
      <path d="M0,115 C200,82 430,58 700,78 L700,400 L0,400 Z" fill="var(--brown)"/>
    </svg>
    <div class="back__name">
      <div class="back__person">Danielle Korrish</div>
      <div class="back__title">PMHNP</div>
    </div>
    <ul class="back__contact">
      <li><span class="label">Fax:</span> 503-418-9152</li>
      <li><span class="label">Phone:</span> 503-418-9267</li>
      <li><span class="label">Email:</span> danielle@dkorrish.com</li>
      <li><span class="label">Website:</span> www.dkorrish.com</li>
      <li>2938 SW Fennick Ave Suite</li>
      <li>340C Portland OR 97225</li>
    </ul>
  </section>

</main>
</body>
</html>
```